Doctor in Veterinary Medecine/ veterinarian

I am a vet and would like a buisness card which is simple yet elegant and professional.
My aim is to help as much animals as I can. My main field of expertise are dogs and cats. I would like the card to reflect a "family doctor" feeling.
It should not be the traditional picture of a paw or a dog but yet it should have a sign of a pet on it. I would like to have my name Lina Haddoul as well as my profession D.V.M and my number.

Target Market(s)

Lebanese population who have pets

Industry/Entity Type

Doctor

Contact Information for Business Card

Should contain my profession " D.V.M", my full name "Lina Haddoul" and my number "0096171539214"

Requirements
Must have
• A certain picture depicting my profession
Nice to have
• Some sort of picture related to pets and animals
Should not have
• A picture of a paw or a dog. I need something more creative

```html
<!DOCTYPE html>
<html lang="en">
<head>
<meta charset="utf-8">
<title>Gentle Haven Clinic – Business Card</title>
<link rel="stylesheet" href="https://fonts.googleapis.com/css2?family=Open+Sans:wght@400;600;700&family=Raleway:wght@400&display=swap">
<style>
  :root {
    --backdrop: #eceeef;
    --card-white: #ffffff;
    --brand-blue: #0b9be0;
    --brand-green: #45ad69;
    --ink: #2b2b2b;
    --ink-soft: #3d3d3d;
    --art-light: #f3f5f6;
    --art-dark: #cfd8dd;
  }
  * { box-sizing: border-box; margin: 0; padding: 0; }
  html, body {
    width: 1200px;
    height: 867px;
    overflow: hidden;
    background: var(--backdrop);
  }
  .business-card {
    position: absolute;
    left: 50px;
    top: 105px;
    width: 1100px;
    height: 658px;
    background: var(--card-white);
    overflow: hidden;
  }
  .card-shapes {
    position: absolute;
    inset: 0;
    width: 100%;
    height: 100%;
  }
  .mascot-art {
    position: absolute;
    left: 72px;
    top: 147px;
    width: 266px;
    height: 409px;
    border-radius: 40px 40px 12px 12px;
    background: linear-gradient(180deg, var(--art-light) 0%, var(--art-dark) 100%);
  }
  .identity {
    position: absolute;
    left: 368px;
    top: 186px;
    width: 624px;
    text-align: center;
  }
  .practice-name {
    font-family: "Open Sans", sans-serif;
    font-weight: 600;
    font-size: 56px;
    line-height: 1.1;
    color: var(--brand-green);
    white-space: nowrap;
  }
  .practice-tagline {
    margin-top: 14px;
    font-family: "Raleway", sans-serif;
    font-size: 30px;
    letter-spacing: 6px;
    color: var(--ink-soft);
  }
  .vet-name {
    margin-top: 30px;
    font-family: "Open Sans", sans-serif;
    font-weight: 700;
    font-size: 33px;
    color: var(--ink);
  }
  .vet-title {
    margin-top: 4px;
    font-family: "Open Sans", sans-serif;
    font-weight: 400;
    font-size: 31px;
    letter-spacing: 2px;
    color: var(--ink-soft);
  }
  .contact-phone {
    position: absolute;
    left: 368px;
    top: 522px;
    width: 624px;
    display: flex;
    justify-content: center;
    align-items: center;
    gap: 8px;
    font-family: "Open Sans", sans-serif;
    font-weight: 600;
    font-size: 37px;
    color: var(--card-white);
  }
  .phone-icon { width: 34px; height: 34px; }
</style>
</head>
<body>
  <div class="business-card">
    <svg class="card-shapes" viewBox="0 0 538 322" preserveAspectRatio="none" aria-hidden="true">
      <path d="M0 0 H538 V68 C430 32 330 14 260 15 C160 17 70 36 0 55 Z" fill="var(--brand-blue)"/>
      <path d="M107 22 C220 6 380 1 538 1 V56 C440 28 340 12 260 13 C200 14 150 17 107 22 Z" fill="var(--brand-green)"/>
      <rect x="0" y="226" width="538" height="96" fill="var(--brand-blue)"/>
    </svg>

    <div class="mascot-art" role="img" aria-label="Illustration of a cat wearing a nurse cap with a stethoscope around its neck"></div>

    <div class="identity">
      <h1 class="practice-name">Gentle Haven Clinic</h1>
      <p class="practice-tagline">VETERINARY CARE</p>
      <p class="vet-name">Lina Haddoul</p>
      <p class="vet-title">D.V.M</p>
    </div>

    <div class="contact-phone">
      <svg class="phone-icon" viewBox="0 0 24 24" aria-hidden="true">
        <path fill="#ffffff" d="M6.6 2.5c.6-.4 1.4-.2 1.8.4l2 3.2c.4.6.2 1.3-.3 1.7l-1.3 1c.7 2 2.2 3.9 4.1 5.1l1.1-1.2c.5-.5 1.2-.6 1.8-.2l3.1 2.1c.6.4.8 1.2.4 1.8l-1.2 2c-.6 1-1.8 1.5-2.9 1.1C9.5 17.8 5.4 12.7 4.3 6.9c-.2-1.1.3-2.2 1.2-2.8z"/>
      </svg>
      <span class="phone-number">0096171539214</span>
    </div>
  </div>
</body>
</html>
```